Finance Broker helping people meet their personal and business goals

New business card design,
1st look at the old business card so this makes sense.
I DON'T want:
the subtext "For all your Rural and Commercial Finance".
I DON'T want the: "and Management Consultant" words
I DON'T want the old phone: 07 49217305
I DON'T want the fax number: 07 48160923
I DON'T want the email address: tallowcreek@quarnet.com.au
I DON'T want the flower
What I DO want
I DO want the mobile 0418 365 907 (in larger text)
I DO want:
My name: Dennis Harlow-Pike
I DO want: Australian Credit Licence 512964 (Tallow Creek Pty Ltd)
I DO want: Principal Finance Broker
I DO want new email: dennis@plantreasurepath.com.au
I DO want address: PO Box 836, Innisfail Qld 4860
I DO want the existing logo (PTP on existing card)

Target Market(s)

Business Borrowers, Home Purchasers, and People wanting to finance cars and plant and equipment

Industry/Entity Type

Financial Service

Contact Information for Business Card

See project description

Font styles to use
Serif

Colors

Designer to choose colors to be used in the design.

Requirements
Must have
• See project description
Nice to have
• Black and Yellow colours
Should not have
• See project description

```html
<!DOCTYPE html>
<html lang="en">
<head>
<meta charset="utf-8">
<title>Plan Treasure Path – Business Card</title>
<link rel="stylesheet" href="https://fonts.googleapis.com/css2?family=Fraunces:opsz,wght@9..144,800&family=Cabin:wght@500;600&family=Oswald:wght@500&display=swap">
<style>
  :root {
    --page: #ffffff;
    --page-edge: #e4e4e4;
    --card-dark: #0a0a0a;
    --card-tone: #3a3a3a;
    --card-mid: #242424;
    --yellow: #fff200;
    --white: #ffffff;
    --band: #5c5c5c;
  }
  * { margin: 0; padding: 0; box-sizing: border-box; }
  html, body {
    width: 1200px; height: 1009px; overflow: hidden;
    background: var(--page);
  }
  .canvas {
    position: relative; width: 1200px; height: 1009px;
    border: 2px solid var(--page-edge);
    background: var(--page);
  }
  .card {
    position: absolute; left: 70px; top: 200px;
    width: 1048px; height: 598px;
    overflow: hidden;
    background: var(--card-dark);
  }
  .card-pattern {
    position: absolute; inset: 0;
    background:
      radial-gradient(ellipse at center, rgba(0,0,0,0.55) 0%, rgba(0,0,0,0) 60%),
      linear-gradient(135deg, var(--card-tone) 0%, var(--card-mid) 50%, var(--card-tone) 100%);
  }
  .line {
    position: absolute; left: 0; width: 100%;
    text-align: center; white-space: nowrap;
  }
  .brand-mark {
    top: 54px;
    font-family: "Fraunces", Georgia, serif; font-weight: 800;
    font-size: 40px; line-height: 52px; color: var(--yellow);
    letter-spacing: 6px;
  }
  .company-name, .person-name {
    font-family: "Fraunces", Georgia, serif; font-weight: 800;
    color: var(--yellow); font-size: 48px; line-height: 54px;
  }
  .company-name { top: 121px; }
  .group-note {
    top: 180px; font-family: "Cabin", Arial, sans-serif; font-weight: 500;
    font-size: 23px; line-height: 30px; color: var(--white);
  }
  .person-name { top: 254px; }
  .licence {
    top: 315px; font-family: "Cabin", Arial, sans-serif; font-weight: 500;
    font-size: 25px; line-height: 32px; color: var(--white);
  }
  .role {
    top: 356px; font-family: "Cabin", Arial, sans-serif; font-weight: 500;
    font-size: 22px; line-height: 28px; color: var(--yellow);
  }
  .phone-band {
    position: absolute; left: 170px; top: 397px; width: 710px; height: 64px;
    background: linear-gradient(90deg, rgba(92,92,92,0) 0%, var(--band) 30%, var(--band) 70%, rgba(92,92,92,0) 100%);
    opacity: 0.85;
  }
  .phone {
    top: 397px; font-family: "Oswald", "Arial Narrow", sans-serif; font-weight: 500;
    font-size: 54px; line-height: 64px; color: var(--white);
  }
  .email, .address {
    font-family: "Cabin", Arial, sans-serif; font-weight: 500;
    font-size: 25px; line-height: 32px; color: var(--white);
  }
  .email { top: 500px; }
  .address { top: 540px; }
</style>
</head>
<body>
<div class="canvas">
  <section class="card">
    <div class="card-pattern" role="img" aria-label="Grey ornamental damask pattern covering the black card background"></div>

    <p class="line brand-mark">PTP</p>
    <h1 class="line company-name">Plan Treasure Path</h1>
    <p class="line group-note">A Member of the Tallow Creek Group</p>

    <h2 class="line person-name">Dennis Harlow-Pike</h2>
    <p class="line licence">Australian Credit Licence 512964</p>
    <p class="line role">Principal Finance Broker</p>

    <div class="phone-band"></div>
    <p class="line phone">04 1836 5907</p>

    <p class="line email">Email : dennis@plantreasurepath.com.au</p>
    <p class="line address">PO Box 836, Innisfail Qld 4860</p>
  </section>
</div>
</body>
</html>
```